Aviation: Overcast Study Guide Book Cover

We need a book cover (front and back) designed for an Instrument Flight Rules (IFR) study guide used by helicopter and airplane pilots to obtain an instrument rating for a helicopter or airplane. Below is the title and subtitles.

TITLE: OVERCAST STUDY GUIDE
SUBTITLE 1: Checkride Preparation for Airplane and Helicopter Pilots
SUBTITLE 2: Prepare for your Instrument Rating with Confidence

We have also upload recommended text to be included on the back cover. In addition, we included images of similar book covers that we like and ones that we do not like. Below are links to two others books by the author.

https://www.bookvarro.example/Rotorcraft-Exam-Handbook-oral-review/dp/507214638K
https://www.bookvarro.example/Manual-Floatwing-Handling-Lionel-Quarrick/dp/5093742816

Flight students

Aviation

• helicopter and airplane

```html
<!DOCTYPE html>
<html lang="en">
<head>
<meta charset="utf-8">
<title>Overcast Study Guide – Cover Spread</title>
<link rel="stylesheet" href="https://fonts.googleapis.com/css2?family=Crimson+Pro:wght@400;600;700&display=swap">
<style>
  :root {
    --page: #ffffff;
    --red-top: #a90e22;
    --red-mid: #d81f34;
    --red-low: #ef3242;
    --gold: #f7c21a;
    --ink: #ffffff;
    --frame: #f0b81c;
    --placeholder: rgba(255, 255, 255, 0.42);
  }
  * { box-sizing: border-box; margin: 0; padding: 0; }
  html, body { width: 1200px; height: 1200px; overflow: hidden; background: var(--page); }
  body { font-family: "Crimson Pro", Georgia, serif; color: var(--ink); position: relative; }

  .spread {
    position: absolute; left: 0; top: 218px; width: 1200px; height: 766px;
    background: linear-gradient(180deg, var(--red-top) 0%, var(--red-mid) 45%, var(--red-low) 100%);
    overflow: hidden;
  }
  .abs { position: absolute; }

  /* Back cover */
  .back-title { left: 60px; width: 478px; top: 52px; text-align: center; color: var(--gold);
    font-weight: 700; font-size: 31px; letter-spacing: 0.3px; }
  .back-tagline { left: 60px; width: 478px; top: 104px; text-align: center; font-size: 15px; }
  .blurb { left: 77px; width: 442px; top: 136px; font-size: 11.6px; line-height: 13.7px; text-align: justify; }
  .blurb p + p { margin-top: 13px; }
  .topics { left: 76px; top: 296px; width: 443px; height: 80px; border: 1.5px solid var(--frame);
    border-radius: 5px; border-collapse: separate; border-spacing: 0; font-size: 11.4px; font-weight: 600; }
  .topics td { border-right: 1px solid var(--frame); border-bottom: 1px solid var(--frame); padding: 0 0 0 9px; height: 26px; white-space: nowrap; }
  .topics tr:last-child td { border-bottom: none; }
  .topics td:last-child { border-right: none; }
  .back-author { left: 60px; width: 478px; top: 390px; text-align: center; font-size: 32px;
    font-variant: small-caps; font-weight: 600; letter-spacing: 1px; }
  .author-photo { left: 67px; top: 442px; width: 147px; height: 200px; background: var(--placeholder); }
  .bio { left: 230px; width: 289px; top: 440px; font-size: 11.4px; line-height: 13.7px; text-align: justify; }

  /* Spine */
  .spine-text { left: 598px; transform-origin: 0 0; transform: rotate(-90deg); white-space: nowrap; }
  .spine-author { top: 198px; font-size: 10px; letter-spacing: 2px; font-variant: small-caps; font-weight: 600; margin-left: -6px; }
  .spine-sub { top: 513px; font-size: 10.2px; margin-left: -6px; }
  .spine-title { top: 720px; font-size: 12px; letter-spacing: 2px; color: var(--gold); font-weight: 700; margin-left: -7px; }

  /* Front cover */
  .front-title { left: 630px; width: 545px; top: 55px; text-align: center; color: var(--gold);
    font-weight: 700; font-size: 41px; letter-spacing: 0.3px; }
  .front-sub { left: 630px; width: 545px; top: 120px; text-align: center; font-size: 30px; line-height: 36px; }
  .front-tagline { left: 630px; width: 545px; top: 216px; text-align: center; font-size: 17.5px; }
  .aircraft-art { left: 716px; top: 288px; width: 413px; height: 353px; }
  .front-author { left: 630px; width: 545px; top: 683px; text-align: center; font-size: 32px;
    font-variant: small-caps; font-weight: 600; letter-spacing: 1px; }
</style>
</head>
<body>
<main class="spread">
  <section class="back-cover">
    <h2 class="abs back-title">OVERCAST STUDY GUIDE</h2>
    <p class="abs back-tagline">Prepare for your IFR check ride with confidence</p>
    <div class="abs blurb">
      <p>Becoming an instrument rated pilot is one of the most challenging ratings to obtain. This guide helps prepare you to pass your IFR check ride with confidence. The question-and-answer format is easy to follow and provides detailed explanations for expanded knowledge.</p>
      <p>Includes Helicopter and Airplane Specific Content<br>This guide is designed to prepare an airplane or helicopter pilot the oral portion of the IFR checkride. Unlike other resources, this guide specifically addresses the differences with IFR flight in helicopters. As a dual rated pilot, the author ensures to identify areas of differences between the two categories of IFR flight. The following concepts are addressed within the guide.</p>
    </div>
    <table class="abs topics">
      <tr><td>• Preflight Actions</td><td>• Enroute Procedures</td><td>• Aeromedical Factors</td></tr>
      <tr><td>• General IFR Concepts</td><td>• Approach Procedures</td><td>• Weather Fundamentals</td></tr>
      <tr><td>• Departure Procedures</td><td>• IFR Emergencies</td><td>• Risk Management</td></tr>
    </table>
    <h3 class="abs back-author">Lionel Quarrick</h3>
    <div class="abs author-photo" role="img" aria-label="Author portrait photograph"></div>
    <p class="abs bio">About the Author: Lionel Quarrick is ATP rated pilot and helicopter and fixed-wing instructor. Lionel is the owner and operator Ridgeline Vector, LLC which does business as Crestwind Aviation and Pike Water Aviation. Crestwind Aviation provides primary helicopter flight instruction while Pike Water Aviation provides seaplane flight instruction and tours. In addition to instructing, Lionel has authored other books to include, The Rotorcraft Exam Handbook, and Manual of Floatwing Handling. Lionel lives in Kentucky with his beautiful wife Marla. They have a daughter, Nora, that is dual rated and employed as a captain for a charter company. Prior to learning to fly, Lionel spent several years in the military as a Special Warfare Combat Craft Crewman in the U.S. Navy and Ranger-qualified infantry officer in the U.S. Army.</p>
  </section>

  <section class="spine">
    <span class="abs spine-text spine-author">Lionel Quarrick</span>
    <span class="abs spine-text spine-sub">Checkride Preparation for Airplane and Helicopter Pilots</span>
    <span class="abs spine-text spine-title">OVERCAST STUDY GUIDE</span>
  </section>

  <section class="front-cover">
    <h1 class="abs front-title">OVERCAST STUDY GUIDE</h1>
    <p class="abs front-sub">Checkride Preparation for<br>Airplane and Helicopter Pilots</p>
    <p class="abs front-tagline">Prepare for your Instrument Rating with Confidence</p>
    <svg class="abs aircraft-art" viewBox="0 0 413 353" role="img" aria-label="Illustration of a climbing airliner, a helicopter and cockpit flight instruments">
      <defs>
        <linearGradient id="artTone" x1="0" y1="0" x2="1" y2="1">
          <stop offset="0" stop-color="#e9ecef" stop-opacity="0.35"/>
          <stop offset="1" stop-color="#9aa3ab" stop-opacity="0.25"/>
        </linearGradient>
      </defs>
      <rect width="413" height="353" rx="8" fill="url(#artTone)"/>
    </svg>
    <h3 class="abs front-author">Lionel Quarrick</h3>
  </section>
</main>
</body>
</html>
```